Business Intelligence / Data Visualization Firm Seeking World Class Power Point Deck

Vane Crest delivers enterprise business intelligence and data visualization solutions enabling clients to see their business as they've never seen it - we transform complex, unstructured data into simple insight that facilitates intelligent decision making, revenue growth and risk reduction. We're seeking a world class power point template for internal, client and conference presentations.

Please visit vanecrest.com for more company context.
*Note: A website photo has been uploaded and may be used or not used - designer discretion.

Additional context:
We use Glimmerdash: https://glimmerdash.harvolo.com/products/predictive-analytics.

Target Market(s)

CXOs at Meridale 100 companies | small and medium business owners (BI / data-viz experts and also decision makers who don't actually understand BI / data-viz).

Industry/Entity Type

Professional Service

Font styles to use
Sans Serif
Other font styles liked:
• Our logo is Expansiva (uploaded), our site is Tahoma. Please use your discretion,.

Colors
ec1f27
ffffff
000000

Requirements
Must have
• PPT format, editable.
• Prefer simple, clean, strong presentation.
Nice to have
• Designs that relate to data, analytics, solutions, automation and transforming complexity into simplicity.
• Reusable icons.

```html
<!DOCTYPE html>
<html lang="en">
<head>
<meta charset="utf-8">
<title>Vane Crest — Presentation Template</title>
<link href="https://fonts.googleapis.com/css2?family=Open+Sans:wght@300;400;600;700&display=swap" rel="stylesheet">
<style>
:root{
  --red:#d3141c;
  --ink:#1b1b1b;
  --dark:#101218;
  --grey:#9a9a9a;
  --bg:#dcdddf;
  --paper:#ffffff;
  --text:#333333;
}
*{box-sizing:border-box;margin:0;padding:0}
html,body{width:1200px;height:900px;overflow:hidden}
body{background:var(--bg);font-family:"Open Sans",Tahoma,sans-serif;color:var(--text)}
.deck{position:absolute;left:164px;top:36px;display:grid;grid-template-columns:repeat(3,287px);grid-auto-rows:161px;column-gap:5px;row-gap:6px}
.slide{position:relative;overflow:hidden;background:var(--paper)}
.title{position:absolute;left:11px;top:12px;font-size:7px;font-weight:400;text-transform:uppercase;color:var(--ink);letter-spacing:-.1px}
.title::after{content:"";display:block;width:14px;height:.6px;background:var(--red);margin-top:1px}
.title.light{color:#fff}
.foot{position:absolute;left:5px;right:7px;bottom:6px;display:flex;align-items:center;gap:2px}
.mark{font-size:4px;font-weight:600;letter-spacing:.9px;color:var(--ink);white-space:nowrap}
.foot .rule{flex:1;height:.5px;background:var(--ink)}
.foot .end{width:4px;height:4px;border-radius:50%;background:var(--red)}
.tx{font-size:3.2px;line-height:1.45;color:var(--text);text-align:justify}
.tx b{display:block;color:var(--ink);font-weight:700}
.red{color:var(--red)}
.ph{position:absolute}

/* cover */
.cover .band{left:0;top:43px;width:287px;height:85px;background:linear-gradient(90deg,#1a2340 0%,#2b3a66 40%,#2c2f44 100%)}
.cover .band-red{position:absolute;right:0;top:38px;width:75px;height:6px;background:var(--red);clip-path:polygon(8% 0,100% 0,100% 100%,0 100%)}
.cover .band-foot{position:absolute;left:150px;top:128px;width:137px;height:3px;background:#c8c8c8}
.cover .welcome{position:absolute;right:10px;top:70px;text-align:right;color:#fff}
.cover .welcome h1{font-size:9px;font-weight:700;letter-spacing:.3px}
.cover .welcome p{font-size:5.5px;letter-spacing:1.2px;font-weight:400}
.cover .welcome small{display:block;font-size:3px;margin-top:1px}
.cover .logo{position:absolute;right:6px;bottom:14px;font-size:9px;font-weight:600;letter-spacing:2.4px;color:var(--ink)}

/* contents */
.contents{background:linear-gradient(160deg,#1e2530 0%,#0e1117 60%,#162130 100%)}
.contents .head{position:absolute;left:31px;top:42px;color:#fff}
.contents .head small{display:block;font-size:3.5px}
.contents .head h2{font-size:10px;font-weight:300}
.contents .head::after{content:"";display:block;width:34px;height:.6px;background:var(--red);margin-top:1px}
.toc{position:absolute;left:48px;top:82px;display:grid;grid-template-columns:100px 100px;row-gap:9px}
.toc li{list-style:none;display:flex;align-items:center;gap:5px;font-size:3.3px;font-weight:700;color:#fff;line-height:1.3}
.toc i{flex:none;width:10px;height:10px;border-radius:50%;background:var(--red);border:1px solid #fff;font-style:normal;font-size:4px;display:flex;align-items:center;justify-content:center}

/* vision */
.vision .top{left:0;top:0;width:287px;height:88px;background:linear-gradient(120deg,#1a1f28 0%,#2e3b4c 55%,#161a22 100%)}
.vision .bottom{position:absolute;left:0;top:88px;width:287px;height:73px;background:var(--red)}
.vision .col{position:absolute;top:67px;width:95px;text-align:center;color:#fff}
.vision .col .ic{width:34px;height:34px;margin:0 auto 5px;border-radius:50%;background:var(--red);border:1.6px solid #fff;display:flex;align-items:center;justify-content:center}
.vision .col p{font-size:4px;line-height:1.35}

/* about */
.about1 .pic{left:15px;top:48px;width:58px;height:38px;background:linear-gradient(135deg,#9bb5cf,#e9eef4 60%,#7a8fa8)}
.about1 .cap{position:absolute;left:15px;top:90px;width:58px;font-size:3.2px;font-weight:700;text-align:center;color:var(--red)}
.about1 .cols{position:absolute;left:85px;top:47px;width:190px;display:grid;grid-template-columns:1fr 1fr;gap:6px 7px}
.about2 .strip{position:absolute;left:0;top:44px;width:93px;height:52px;background:var(--red);color:#fff;font-size:3.3px;font-weight:700;line-height:1.35;padding:17px 11px}
.about2 .pic{left:93px;top:44px;width:194px;height:52px;background:linear-gradient(90deg,#2031a8,#3b63d8 55%,#8fb5f0)}
.about2 .body{position:absolute;left:93px;top:103px;width:180px}
.about2 .body p+p{margin-top:4px}
.about3 .row{position:absolute;left:33px;top:46px;display:grid;grid-template-columns:repeat(3,69px);gap:6px}
.about3 .pic{position:relative;height:46px}
.about3 .cap{font-size:3.2px;font-weight:700;color:var(--red);margin:4px 0 2px}

/* infograph 1 */
.tiles{position:absolute;left:23px;top:45px;display:grid;grid-template-columns:repeat(4,58px);gap:2px}
.tile .up{height:35px;display:flex;flex-direction:column;align-items:center;justify-content:flex-end;padding-bottom:3px;color:#fff;font-size:3.5px;font-weight:700;text-align:center;line-height:1.2}
.tile .up .ic{width:12px;height:12px;margin-bottom:4px;border:1px solid #fff;border-radius:50%}
.tile .down{height:52px;padding:8px 4px;color:#fff;font-size:3.2px;font-weight:700;text-align:center;line-height:1.4}
.bg-red{background:var(--red)}
.bg-ink{background:#0a0a0a}

/* infograph lists */
.list{position:absolute;width:62px}
.list .it{margin-bottom:7px}
.list h4{font-size:4.2px;font-weight:600;color:var(--ink);display:flex;align-items:center;gap:3px}
.list h4.red{color:var(--red)}
.list h4 .dot{width:5px;height:5px;border-radius:50%;border:1px solid currentColor}
.list p{font-size:2.9px;line-height:1.4;text-align:center;margin-top:2px}

/* team */
.team .row{position:absolute;left:25px;top:52px;display:grid;grid-template-columns:repeat(3,70px);gap:20px;text-align:center}
.team .av{width:34px;height:34px;margin:0 auto 4px;border-radius:50%;border:1.4px solid var(--red);background:radial-gradient(circle at 50% 40%,#e6e6e6,#9c9c9c)}
.team h5{font-size:3.6px;font-weight:700;color:var(--ink)}
.team em{display:block;font-size:2.8px;margin-bottom:4px}

/* chart */
.chart1 .body{position:absolute;left:19px;top:43px;width:128px}
.chart1 .body p{margin-bottom:4px}
.chart1 .body .k{color:var(--red);font-weight:700}
.legend{position:absolute;left:193px;top:92px;font-size:2.8px;line-height:1.35}
.legend div{display:flex;gap:3px;margin-bottom:3px}
.legend i{flex:none;width:3px;height:3px;margin-top:.5px}
.donuts{position:absolute;left:24px;top:48px;display:grid;grid-template-columns:repeat(3,70px);gap:10px;text-align:center}
.donuts p{font-size:2.9px;line-height:1.4;margin-top:6px}

/* section */
.section{background:radial-gradient(circle at 50% 45%,#1c2638 0%,#0b0f18 70%)}
.section .ic{position:absolute;left:125px;top:64px;width:37px;height:37px;border-radius:50%;background:var(--red);color:#fff;font-size:24px;font-weight:700;font-style:italic;display:flex;align-items:center;justify-content:center;font-family:Georgia,serif}
.section h3{position:absolute;left:0;right:0;top:113px;text-align:center;color:#fff;font-size:10px;font-weight:300}

/* image text */
.imgtext .left{position:absolute;left:0;top:0;width:139px;height:161px;background:var(--red);color:#fff}
.imgtext .pic{left:139px;top:0;width:148px;height:161px;background:linear-gradient(180deg,#e7eef6,#b9c9db 60%,#8c9eb3)}
.imgtext .left .tx{color:#fff;font-weight:700;position:absolute;left:15px;top:54px;width:110px}
.imgtext .left .tx+ .tx{top:108px}
.imgtext .mark{position:absolute;left:3px;bottom:4px;color:#fff}

/* thanks */
.thanks .logo{position:absolute;left:16px;top:33px;font-size:9.5px;font-weight:600;letter-spacing:2.6px;color:var(--ink)}
.thanks .redline{position:absolute;right:0;top:59px;width:88px;height:3px;background:var(--red)}
.thanks .pic{left:0;top:62px;width:287px;height:99px;background:linear-gradient(90deg,#0d141c 0%,#1a2836 55%,#2b3742 100%)}
.thanks .msg{position:absolute;left:17px;top:80px;font-size:6px;font-weight:300;line-height:1.3;color:#fff}
.thanks .msg span{color:var(--red);display:block}
.thanks .contact{position:absolute;left:17px;top:108px;list-style:none;color:#fff;font-size:3.6px}
.thanks .contact li{display:flex;align-items:center;gap:4px;margin-bottom:5px}
.thanks .contact i{width:6px;height:6px;border-radius:50%;background:var(--red)}
</style>
</head>
<body>
<main class="deck">

  <!-- 1 Cover -->
  <section class="slide cover">
    <div class="ph band" role="img" aria-label="Close-up photo of a red eye over blue data code"></div>
    <div class="band-red"></div>
    <div class="band-foot"></div>
    <div class="welcome">
      <h1>WELCOME</h1>
      <p>TO OUR PRESENTATION</p>
      <small>Birmingham, March 25, 2011</small>
    </div>
    <div class="logo">VANE CREST</div>
  </section>

  <!-- 2 Contents -->
  <section class="slide contents">
    <div class="head"><small>TABLE OF</small><h2>CONTENTS</h2></div>
    <ul class="toc">
      <li><i>1</i>LOREM IPSUM DOLOR SIT<br>MET DOLOR SIT MET</li>
      <li><i>1</i>LOREM IPSUM DOLOR SIT<br>MET DOLOR SIT MET</li>
      <li><i>1</i>LOREM IPSUM DOLOR SIT<br>MET DOLOR SIT MET</li>
      <li><i>1</i>LOREM IPSUM DOLOR SIT<br>MET DOLOR SIT MET</li>
      <li><i>1</i>LOREM IPSUM DOLOR SIT<br>MET DOLOR SIT MET</li>
      <li><i>1</i>LOREM IPSUM DOLOR SIT<br>MET DOLOR SIT MET</li>
    </ul>
  </section>

  <!-- 3 Vision & Mission -->
  <section class="slide vision">
    <div class="ph top" role="img" aria-label="Photo of a hand drawing a rising business chart"></div>
    <div class="bottom"></div>
    <h2 class="title light" style="top:13px">VISION &amp; MISSION</h2>
    <div class="col" style="left:24px">
      <div class="ic"><svg width="16" height="10" viewBox="0 0 16 10"><circle cx="4" cy="5" r="3.2" fill="none" stroke="#fff" stroke-width="1.6"/><circle cx="12" cy="5" r="3.2" fill="none" stroke="#fff" stroke-width="1.6"/><rect x="6.5" y="3.6" width="3" height="1.6" fill="#fff"/></svg></div>
      <p>To provide state of the art logistical and supply chain solutions to the defined needs of our customers using the best people, processes and systems in creating efficient and effective results.</p>
    </div>
    <div class="col" style="left:170px">
      <div class="ic"><svg width="16" height="12" viewBox="0 0 16 12"><path d="M2 11a6 6 0 1 1 12 0" fill="none" stroke="#fff" stroke-width="1.6"/><path d="M8 10l3-5" stroke="#fff" stroke-width="1.4"/></svg></div>
      <p>To provide state of the art logistical and supply chain solutions to the defined needs of our customers using the best people, processes and systems in creating efficient and effective results.</p>
    </div>
  </section>

  <!-- 4 About us -->
  <section class="slide about1">
    <h2 class="title">ABOUT US</h2>
    <div class="ph pic" role="img" aria-label="Photo of a hand touching network icons"></div>
    <p class="cap">Lorem ipsum dolor sit amet consectetur adipisicing elit sed do eiusmod</p>
    <div class="cols">
      <p class="tx"><b>Lorem ipsum dolor sit amet</b>consectetur adipisicing elit, sed do eiusmod tempor incididunt ut labore et dolore magna aliqua. Ut enim ad minim veniam, quis nostrud exercitation ullamco laboris nisi ut aliquip ex ea commodo consequat. Duis aute irure dolor in reprehenderit in voluptate velit esse cillum dolore eu fugiat nulla pariatur.</p>
      <p class="tx"><b>Lorem ipsum dolor sit amet</b>consectetur adipisicing elit, sed do eiusmod tempor incididunt ut labore et dolore magna aliqua. Ut enim ad minim veniam, quis nostrud exercitation ullamco laboris nisi ut aliquip ex ea commodo consequat. Duis aute irure dolor in reprehenderit in voluptate velit esse cillum dolore eu fugiat nulla pariatur.</p>
      <p class="tx"><b>Lorem ipsum dolor sit amet</b>consectetur adipisicing elit, sed do eiusmod tempor incididunt ut labore et dolore magna aliqua. Ut enim ad minim veniam, quis nostrud exercitation ullamco laboris nisi ut aliquip ex ea</p>
      <p class="tx"><b>Lorem ipsum dolor sit amet</b>consectetur adipisicing elit, sed do eiusmod tempor incididunt ut labore et dolore magna aliqua. Ut enim ad minim veniam, quis nostrud exercitation ullamco laboris nisi ut aliquip ex ea</p>
    </div>
    <div class="foot"><span class="mark">VANE CREST</span><span class="rule"></span><span class="end"></span></div>
  </section>

  <!-- 5 About us -->
  <section class="slide about2">
    <h2 class="title">ABOUT US</h2>
    <div class="strip">LOREM IPSUM DOLOR SIT MET CONSECTUR ADIPISCING ELIT, SED DO EIUSMOD TEMPOR INCIDIDUNT UT LABORE ET DOLORE MAGNA</div>
    <div class="ph pic" role="img" aria-label="Illustration of data analysis screens and a light bulb"></div>
    <div class="body">
      <p class="tx">Lorem ipsum dolor sit amet, consectetur adipisicing elit, sed do eiusmod tempor incididunt ut labore et dolore magna aliqua. Ut enim ad minim veniam, quis nostrud exercitation ullamco laboris nisi ut aliquip ex ea commodo consequat. Duis aute irure dolor in reprehenderit in voluptate velit esse cillum dolore eu fugiat nulla pariatur.</p>
      <p class="tx">Lorem ipsum dolor sit amet, consectetur adipisicing elit, sed do eiusmod tempor incididunt ut labore et dolore magna aliqua. Ut enim ad minim veniam, quis nostrud exercitation ullamco</p>
    </div>
    <div class="foot"><span class="mark">VANE CREST</span><span class="rule"></span><span class="end"></span></div>
  </section>

  <!-- 6 About us -->
  <section class="slide about3">
    <h2 class="title">ABOUT US</h2>
    <div class="row">
      <div>
        <div class="ph pic" role="img" aria-label="Photo of hands holding a glowing globe" style="background:linear-gradient(135deg,#0f2c52,#3f8ad0)"></div>
        <p class="cap">Lorem ipsum dolor sit amet</p>
        <p class="tx">Ut enim ad minim veniam, quis nostrud exercitation ullamco laboris nisi ut aliquip ex ea commodo consequat. Duis aute irure dolor in reprehenderit in voluptate velit esse cillum dolore eu fugiat nulla pariatur.</p>
      </div>
      <div>
        <div class="ph pic" role="img" aria-label="Illustration of a padlock on a circuit board" style="background:linear-gradient(135deg,#1a5ea8,#8cc1ec)"></div>
        <p class="cap">Lorem ipsum dolor sit amet</p>
        <p class="tx">Ut enim ad minim veniam, quis nostrud exercitation ullamco laboris nisi ut aliquip ex ea commodo consequat. Duis aute irure dolor in reprehenderit in voluptate velit esse cillum dolore eu fugiat nulla pariatur.</p>
      </div>
      <div>
        <div class="ph pic" role="img" aria-label="Blue digital numbers background" style="background:linear-gradient(135deg,#0a1a3a,#1d4a8a)"></div>
        <p class="cap">Lorem ipsum dolor sit amet</p>
        <p class="tx">Ut enim ad minim veniam, quis nostrud exercitation ullamco laboris nisi ut aliquip ex ea commodo consequat. Duis aute irure dolor in reprehenderit in voluptate velit esse cillum dolore eu fugiat nulla pariatur.</p>
      </div>
    </div>
    <div class="foot"><span class="mark">VANE CREST</span><span class="rule"></span><span class="end"></span></div>
  </section>

  <!-- 7 Infograph tiles -->
  <section class="slide">
    <h2 class="title">INFOGRAPH</h2>
    <div class="tiles">
      <div class="tile"><div class="up bg-red"><span class="ic"></span>MANAGEMENT<br>SOLUTIONS</div><div class="down bg-ink">Dolor sit amet, consectetur adipisicing elit, sed do eiusmod tempor incididunt ut labore et dolore magna aliqua.</div></div>
      <div class="tile"><div class="up bg-ink"><span class="ic"></span>INFORMATION<br>SOLUTIONS</div><div class="down bg-red">Dolor sit amet, consectetur adipisicing elit, sed do eiusmod tempor incididunt ut labore et dolore magna aliqua.</div></div>
      <div class="tile"><div class="up bg-red"><span class="ic"></span>PROFESSIONAL<br>SERVICES</div><div class="down bg-ink">Dolor sit amet, consectetur adipisicing elit, sed do eiusmod tempor incididunt ut labore et dolore magna aliqua.</div></div>
      <div class="tile"><div class="up bg-ink"><span class="ic"></span>ORGANIZATIONAL<br>TRANSFORMATION</div><div class="down bg-red">Dolor sit amet, consectetur adipisicing elit, sed do eiusmod tempor incididunt ut labore et dolore magna aliqua.</div></div>
    </div>
    <div class="foot"><span class="mark">VANE CREST</span><span class="rule"></span><span class="end"></span></div>
  </section>

  <!-- 8 Infograph horseshoe -->
  <section class="slide">
    <h2 class="title">INFOGRAPH</h2>
    <div class="list" style="left:26px;top:45px">
      <div class="it"><h4 class="red"><span class="dot"></span>Lorem Ipsum</h4><p>Dolor sit amet, consectetur adipisicing elit, sed do eiusmod tempor</p></div>
      <div class="it"><h4><span class="dot"></span>Lorem Ipsum</h4><p>Dolor sit amet, consectetur adipisicing elit, sed do eiusmod tempor</p></div>
      <div class="it"><h4 class="red"><span class="dot"></span>Lorem Ipsum</h4><p>Dolor sit amet, consectetur adipisicing elit, sed do eiusmod tempor</p></div>
    </div>
    <svg style="position:absolute;left:103px;top:47px" width="80" height="80" viewBox="0 0 80 80" aria-hidden="true">
      <g fill="none" stroke-width="19" stroke-dasharray="17.3 133.5">
        <circle cx="40" cy="40" r="24" stroke="#d3141c" transform="rotate(135 40 40)"/>
        <circle cx="40" cy="40" r="24" stroke="#0a0a0a" transform="rotate(180 40 40)"/>
        <circle cx="40" cy="40" r="24" stroke="#d3141c" transform="rotate(225 40 40)"/>
        <circle cx="40" cy="40" r="24" stroke="#0a0a0a" transform="rotate(270 40 40)"/>
        <circle cx="40" cy="40" r="24" stroke="#d3141c" transform="rotate(315 40 40)"/>
        <circle cx="40" cy="40" r="24" stroke="#0a0a0a" transform="rotate(0 40 40)"/>
      </g>
    </svg>
    <div class="list" style="left:204px;top:45px">
      <div class="it"><h4><span class="dot"></span>Lorem Ipsum</h4><p>Dolor sit amet, consectetur adipisicing elit, sed do eiusmod tempor</p></div>
      <div class="it"><h4 class="red"><span class="dot"></span>Lorem Ipsum</h4><p>Dolor sit amet, consectetur adipisicing elit, sed do eiusmod tempor</p></div>
      <div class="it"><h4><span class="dot"></span>Lorem Ipsum</h4><p>Dolor sit amet, consectetur adipisicing elit, sed do eiusmod tempor</p></div>
    </div>
    <div class="foot"><span class="mark">VANE CREST</span><span class="rule"></span><span class="end"></span></div>
  </section>

  <!-- 9 Infograph ring -->
  <section class="slide">
    <h2 class="title">INFOGRAPH</h2>
    <div class="list" style="left:26px;top:47px">
      <div class="it" style="margin-bottom:14px"><h4><span class="dot"></span>Lorem Ipsum</h4><p>Dolor sit amet, consectetur adipisicing elit, sed do eiusmod tempor</p></div>
      <div class="it"><h4 class="red"><span class="dot"></span>Lorem Ipsum</h4><p>Dolor sit amet, consectetur adipisicing elit, sed do eiusmod tempor</p></div>
    </div>
    <svg style="position:absolute;left:100px;top:37px" width="96" height="96" viewBox="0 0 80 80" aria-hidden="true">
      <g fill="none" stroke-width="20" stroke-dasharray="35.7 115.1">
        <circle cx="40" cy="40" r="24" stroke="#0a0a0a" transform="rotate(-90 40 40)"/>
        <circle cx="40" cy="40" r="24" stroke="#d3141c" transform="rotate(0 40 40)"/>
        <circle cx="40" cy="40" r="24" stroke="#0a0a0a" transform="rotate(90 40 40)"/>
        <circle cx="40" cy="40" r="24" stroke="#d3141c" transform="rotate(180 40 40)"/>
      </g>
      <g fill="#fff" stroke="#d3141c" stroke-width=".8">
        <circle cx="57" cy="23" r="6"/><circle cx="57" cy="57" r="6"/><circle cx="23" cy="57" r="6"/><circle cx="23" cy="23" r="6"/>
      </g>
      <g fill="#d3141c"><circle cx="57" cy="23" r="1.6"/><circle cx="57" cy="57" r="1.6"/><circle cx="23" cy="57" r="1.6"/><circle cx="23" cy="23" r="1.6"/></g>
    </svg>
    <div class="list" style="left:206px;top:47px">
      <div class="it" style="margin-bottom:14px"><h4 class="red"><span class="dot"></span>Lorem Ipsum</h4><p>Dolor sit amet, consectetur adipisicing elit, sed do eiusmod tempor</p></div>
      <div class="it"><h4><span class="dot"></span>Lorem Ipsum</h4><p>Dolor sit amet, consectetur adipisicing elit, sed do eiusmod tempor</p></div>
    </div>
    <div class="foot"><span class="mark">VANE CREST</span><span class="rule"></span><span class="end"></span></div>
  </section>

  <!-- 10 Team -->
  <section class="slide team">
    <h2 class="title">TEAM</h2>
    <div class="row">
      <div><div class="av" role="img" aria-label="Portrait photo of Jonathan Doe"></div><h5>JONATHAN DOE</h5><em>President</em><p class="tx" style="text-align:center">dolor sit amet, consectetur adipisicing elit, sed do eiusmod tempor incididunt ut labore et dolore magna aliqua. Ut enim ad minim veniam, quis nostrud exercitation ullamco laboris nisi ut aliquip ex ea commodo consequat fugiat nulla pariatur.</p></div>
      <div><div class="av" role="img" aria-label="Portrait photo of Melanie Doe"></div><h5>MELANIE DOE</h5><em>CEO / Founder</em><p class="tx" style="text-align:center">dolor sit amet, consectetur adipisicing elit, sed do eiusmod tempor incididunt ut labore et dolore magna aliqua. Ut enim ad minim veniam, quis nostrud exercitation ullamco laboris nisi ut aliquip ex ea commodo consequat fugiat nulla pariatur.</p></div>
      <div><div class="av" role="img" aria-label="Portrait photo of Natalie Doe"></div><h5>NATALIE DOE</h5><em>Vice President</em><p class="tx" style="text-align:center">dolor sit amet, consectetur adipisicing elit, sed do eiusmod tempor incididunt ut labore et dolore magna aliqua. Ut enim ad minim veniam, quis nostrud exercitation ullamco laboris nisi ut aliquip ex ea commodo consequat fugiat nulla pariatur.</p></div>
    </div>
    <div class="foot"><span class="mark">VANE CREST</span><span class="rule"></span><span class="end"></span></div>
  </section>

  <!-- 11 Bar chart -->
  <section class="slide chart1">
    <h2 class="title">CHART</h2>
    <div class="body">
      <p class="tx"><span class="k">Lorem ipsum dolor sit amet</span><br>consectetur adipisicing elit, sed do eiusmod tempor incididunt ut labore et dolore magna aliqua. Ut enim ad minim veniam, quis nostrud exercitation ullamco laboris nisi ut aliquip ex ea commodo consequat. Duis aute irure dolor in reprehenderit in voluptate velit esse cillum dolore eu fugiat nulla pariatur.</p>
      <p class="tx"><span class="k">Lorem ipsum dolor sit amet</span><br>consectetur adipisicing elit, sed do eiusmod tempor incididunt ut labore et dolore magna aliqua. Ut enim ad minim veniam, quis nostrud exercitation ullamco laboris nisi ut aliquip ex ea commodo consequat. Duis aute irure dolor in reprehenderit in voluptate velit esse cillum dolore eu</p>
      <p class="tx"><span class="k">Lorem ipsum dolor sit amet</span><br>Excepteur sint occaecat cupidatat non proident, sunt in culpa qui officia deserunt mollit anim id est laborum.</p>
    </div>
    <svg style="position:absolute;left:176px;top:30px" width="88" height="58" viewBox="0 0 88 58" aria-label="Bar chart 2009 to 2012" role="img">
      <line x1="6" y1="2" x2="6" y2="48" stroke="#999" stroke-width=".4"/>
      <line x1="6" y1="48" x2="84" y2="48" stroke="#999" stroke-width=".4"/>
      <g>
        <rect x="10" y="22" width="4" height="26" fill="#d3141c"/><rect x="14" y="30" width="4" height="18" fill="#0a0a0a"/><rect x="18" y="37" width="4" height="11" fill="#bbb"/>
        <rect x="29" y="28" width="4" height="20" fill="#d3141c"/><rect x="33" y="24" width="4" height="24" fill="#0a0a0a"/><rect x="37" y="36" width="4" height="12" fill="#bbb"/>
        <rect x="48" y="17" width="4" height="31" fill="#d3141c"/><rect x="52" y="27" width="4" height="21" fill="#0a0a0a"/><rect x="56" y="33" width="4" height="15" fill="#bbb"/>
        <rect x="67" y="30" width="4" height="18" fill="#d3141c"/><rect x="71" y="14" width="4" height="34" fill="#0a0a0a"/><rect x="75" y="36" width="4" height="12" fill="#bbb"/>
      </g>
      <rect x="36" y="8" width="6" height="3" fill="#bbb"/><rect x="47" y="12" width="6" height="3" fill="#d3141c"/><rect x="70" y="9" width="6" height="3" fill="#0a0a0a"/>
      <g font-size="3" fill="#333" font-family="Open Sans,sans-serif"><text x="11" y="54">2009</text><text x="30" y="54">2010</text><text x="49" y="54">2011</text><text x="68" y="54">2012</text></g>
    </svg>
    <div class="legend">
      <div><i style="background:#d3141c"></i><span><b>LOREM IPSUM</b><br>lorem ipsum dolor sit amet consectetur adipisicing elit sed do eiusmod</span></div>
      <div><i style="background:#bbb"></i><span><b>LOREM IPSUM</b><br>lorem ipsum dolor sit amet consectetur adipisicing elit sed do eiusmod</span></div>
      <div><i style="background:#0a0a0a"></i><span><b>LOREM IPSUM</b></span></div>
    </div>
    <div class="foot"><span class="mark">VANE CREST</span><span class="rule"></span><span class="end"></span></div>
  </section>

  <!-- 12 Donut charts -->
  <section class="slide">
    <h2 class="title">CHART</h2>
    <div class="donuts">
      <div>
        <svg width="38" height="38" viewBox="0 0 38 38" role="img" aria-label="81 percent">
          <circle cx="19" cy="19" r="15" fill="none" stroke="#0a0a0a" stroke-width="4"/>
          <circle cx="19" cy="19" r="15" fill="none" stroke="#d3141c" stroke-width="4" stroke-dasharray="76.3 94.2" transform="rotate(-90 19 19)"/>
          <text x="19" y="21.2" text-anchor="middle" font-size="6.5" font-weight="700" fill="#d3141c" font-family="Open Sans,sans-serif">81%</text>
        </svg>
        <p>dolor sit amet, consectetur adipisicing elit, sed do eiusmod tempor incididunt ut labore et dolore magna aliqua. Ut enim ad minim veniam, quis nostrud exercitation ullamco laboris nisi fugiat nulla pariatur.</p>
      </div>
      <div>
        <svg width="38" height="38" viewBox="0 0 38 38" role="img" aria-label="72 percent">
          <circle cx="19" cy="19" r="15" fill="none" stroke="#0a0a0a" stroke-width="4"/>
          <circle cx="19" cy="19" r="15" fill="none" stroke="#d3141c" stroke-width="4" stroke-dasharray="67.9 94.2" transform="rotate(-90 19 19)"/>
          <text x="19" y="21.2" text-anchor="middle" font-size="6.5" font-weight="700" fill="#d3141c" font-family="Open Sans,sans-serif">72%</text>
        </svg>
        <p>dolor sit amet, consectetur adipisicing elit, sed do eiusmod tempor incididunt ut labore et dolore magna aliqua. Ut enim ad minim veniam, quis nostrud exercitation ullamco laboris nisi fugiat nulla pariatur.</p>
      </div>
      <div>
        <svg width="38" height="38" viewBox="0 0 38 38" role="img" aria-label="63 percent">
          <circle cx="19" cy="19" r="15" fill="none" stroke="#0a0a0a" stroke-width="4"/>
          <circle cx="19" cy="19" r="15" fill="none" stroke="#d3141c" stroke-width="4" stroke-dasharray="59.4 94.2" transform="rotate(-90 19 19)"/>
          <text x="19" y="21.2" text-anchor="middle" font-size="6.5" font-weight="700" fill="#d3141c" font-family="Open Sans,sans-serif">63%</text>
        </svg>
        <p>dolor sit amet, consectetur adipisicing elit, sed do eiusmod tempor incididunt ut labore et dolore magna aliqua. Ut enim ad minim veniam, quis nostrud exercitation ullamco laboris nisi fugiat nulla pariatur.</p>
      </div>
    </div>
    <div class="foot"><span class="mark">VANE CREST</span><span class="rule"></span><span class="end"></span></div>
  </section>

  <!-- 13 Section title -->
  <section class="slide section" role="img" aria-label="Dark background of large blue digital numbers">
    <div class="ic">i</div>
    <h3>SECTION TITLE</h3>
  </section>

  <!-- 14 Image text -->
  <section class="slide imgtext">
    <div class="left">
      <h2 class="title light" style="top:12px">IMAGE TEXT</h2>
      <p class="tx">Lorem ipsum dolor sit amet, consectetur adipisicing elit, sed do eiusmod tempor incididunt ut labore et dolore magna aliqua. Ut enim ad minim veniam, quis nostrud exercitation ullamco laboris nisi ut aliquip ex ea commodo consequat. Duis aute irure dolor in reprehenderit in voluptate velit esse cillum dolore eu fugiat nulla pariatur.</p>
      <p class="tx">Lorem ipsum dolor sit amet, consectetur adipisicing elit, sed do eiusmod tempor incididunt ut labore et dolore magna</p>
      <span class="mark">VANE CREST</span>
    </div>
    <div class="ph pic" role="img" aria-label="Photo of a businessman facing a wall of data charts"></div>
  </section>

  <!-- 15 Thank you -->
  <section class="slide thanks">
    <div class="logo">VANE CREST</div>
    <div class="redline"></div>
    <div class="ph pic" role="img" aria-label="Close-up photo of an eye over binary code"></div>
    <p class="msg"><span>THANK YOU</span>FOR YOUR TIME</p>
    <ul class="contact">
      <li><i></i>418 Harrow Lane Ste 12</li>
      <li><i></i>support@vanecrest.com</li>
      <li><i></i>www.vanecrest.com</li>
    </ul>
  </section>

</main>
</body>
</html>
```